Update Old OR create new Website

Current Website is looking a bit old, I did this one a few years back.

Would like a fresh new look, current website wordpress theme is " the Lumora theme" from plexmarkett and I just purchased this theme - "vendrop" also from plexmarkett, I quite like the look of - http://vendrop.qorvan-skins.com/tech-business/ and if we could get somthing simlar would be great.

current website is at http://www.zem.com.au, have been playing around with the slider that i like.

I have said 5 pages to be designed but really it is just a 5 page website where most pages will look the same.

Any questions please let me know

Target Market(s)

Business

Coding

Coded - Design and coding required

Number of Pages Required

5+ page

Font styles to use
Sans Serif

Colors
33a6d7
0292cd
ffffff
0255a3

Requirements
Must have
• Device compatibility - pc, tablet, phone
Nice to have
• video
Should not have
• vunerabilities. Must also use images that will expire or disappear, ie must be uploaded to site not links to elsewhere.

```html
<!DOCTYPE html>
<html lang="en">
<head>
<meta charset="utf-8">
<title>ZEM Technologies</title>
<link href="https://fonts.googleapis.com/css2?family=Lato:wght@400;700&family=Oswald:wght@400&family=Roboto+Condensed:wght@300;400&display=swap" rel="stylesheet">
<style>
:root{
  --blue:#0ea5d6;
  --blue-deep:#0292cd;
  --navy:#0255a3;
  --white:#ffffff;
  --ink:#222222;
  --text:#555555;
  --muted:#888888;
  --topbar:#333333;
  --light:#ebebeb;
  --footer:#353a46;
  --footer-deep:#2a2e37;
  --footer-text:#9aa0ab;
}
*{box-sizing:border-box;margin:0;padding:0}
html,body{width:1200px;height:2525px;overflow:hidden}
body{font-family:'Lato',sans-serif;color:var(--text);background:var(--white);position:relative}
.wrap{position:relative;width:1200px}

/* top bar */
.topbar{height:34px;background:var(--topbar);color:#ddd;font-size:13px;position:relative}
.topbar .contact{position:absolute;left:79px;top:9px;display:flex;gap:22px;align-items:center}
.topbar .contact span{display:flex;align-items:center;gap:7px}
.topbar .social{position:absolute;left:830px;top:7px;display:flex;gap:6px}
.social i{display:block;width:20px;height:20px;border-radius:50%;background:#6d7480}
.call-now{position:absolute;left:941px;top:0;width:178px;height:34px;background:var(--blue);color:var(--white);font-family:'Roboto Condensed',sans-serif;font-size:15px;line-height:34px;text-align:center}

/* header */
.header{height:107px;background:var(--white);position:relative;border-bottom:1px solid #eee}
.brand{position:absolute;left:79px;top:36px;display:flex;align-items:center;gap:10px}
.brand .mark{width:34px;height:34px;background:var(--blue)}
.brand .name{font-family:'Lato',sans-serif;font-weight:700;font-size:24px;color:var(--ink)}
.nav{position:absolute;top:44px;left:0;width:1200px;font-family:'Roboto Condensed',sans-serif;font-size:16px;color:#333}
.nav a{position:absolute;color:inherit;text-decoration:none}
.nav .sep{position:absolute;top:2px;width:1px;height:16px;background:#ccc}

/* hero */
.hero{height:493px;position:relative;background:linear-gradient(100deg,#8fb3cc 0%,#b8d2e3 35%,#d9e6ef 55%,#5e88a8 75%,#c79a83 90%,#e2b49b 100%)}
.hero h1{position:absolute;left:79px;top:168px;font-family:'Oswald',sans-serif;font-weight:400;font-size:33px;line-height:42px;color:var(--white);letter-spacing:.3px}
.hero .dots{position:absolute;left:81px;top:288px;display:flex;gap:6px}
.dots i{display:block;width:12px;height:12px;border-radius:50%;background:var(--white)}
.hero .dots i:first-child{border:3px solid var(--white);background:var(--blue)}

/* services */
.services{height:396px;position:relative;background:var(--white)}
.service{position:absolute;top:61px;width:224px;height:273px;border:1px solid #ddd;border-bottom:5px solid #2b2b2b;text-align:center;background:var(--white)}
.service svg.icon{position:absolute;left:72px;top:30px}
.service h3{position:absolute;top:133px;width:100%;font-family:'Roboto Condensed',sans-serif;font-weight:400;font-size:18px;color:var(--ink)}
.service p{position:absolute;top:162px;left:20px;right:20px;font-size:12.5px;line-height:17px;color:var(--muted)}
.service .more{position:absolute;left:92px;bottom:-5px;width:40px;height:20px;border-radius:20px 20px 0 0;background:#2b2b2b;color:var(--white);font-size:16px;line-height:22px;font-weight:700}

/* about */
.about{height:380px;background:var(--light);position:relative}
.section-title{font-family:'Roboto Condensed',sans-serif;font-weight:400;font-size:28px;color:var(--ink)}
.section-title em{font-style:normal;color:var(--blue)}
.about h2{position:absolute;left:79px;top:50px}
.rule{position:absolute;height:2px;width:66px;background:#bbb}
.about .rule{left:81px;top:107px}
.about .copy{position:absolute;left:79px;top:126px;width:505px;font-size:14.5px;line-height:27px;color:#444}
.about .copy p+p{margin-top:10px}
.btn{position:absolute;left:81px;top:291px;width:128px;height:39px;background:var(--blue);color:var(--white);font-family:'Roboto Condensed',sans-serif;font-size:16px;line-height:39px;text-align:center}
.about .frame{position:absolute;left:889px;top:49px;width:230px;height:200px;background:var(--blue)}
.about .photo{position:absolute;left:626px;top:61px;width:485px;height:269px;background:linear-gradient(90deg,#9aa3ad,#c8ced4 45%,#7c8590 70%,#b7bec6)}

/* testimonials */
.testimonials{height:530px;position:relative;background:linear-gradient(120deg,#2a2e33 0%,#4a4e52 35%,#3a3d41 60%,#1f2226 100%)}
.testimonials h2{position:absolute;width:1200px;top:48px;text-align:center;color:var(--white)}
.testimonials .rule{left:567px;top:103px;background:#9a9a9a}
.quote{position:absolute;top:135px;width:333px;height:200px;background:rgba(15,15,15,.75);padding:20px 20px}
.quote svg{display:block;margin-bottom:10px}
.quote p{font-size:13.5px;line-height:24px;color:var(--white)}
.author{position:absolute;top:372px;display:flex;align-items:center;gap:13px}
.author .avatar{width:54px;height:54px;border-radius:50%;background:#c9c3bd;border:2px solid var(--white)}
.author strong{display:block;font-family:'Roboto Condensed',sans-serif;font-weight:400;font-size:17px;color:var(--white)}
.author span{font-size:13px;color:#ddd}
.testimonials .dots{position:absolute;left:575px;top:466px;display:flex;gap:8px}
.testimonials .dots i{width:9px;height:9px}
.testimonials .dots i:first-child{width:16px;border-radius:5px;background:var(--blue)}

/* partners */
.partners{height:250px;position:relative;background:var(--white)}
.partners h2{position:absolute;width:1200px;top:38px;text-align:center}
.partners .rule{left:567px;top:90px}
.partner{position:absolute;top:130px;width:148px;height:78px;border:1px solid #cfcfcf;display:flex;align-items:center;justify-content:center}
.partner i{display:block;width:96px;height:26px;border-radius:4px;background:#d5d5d5}

/* footer */
.footer{height:281px;background:var(--footer);position:relative;color:var(--footer-text)}
.footer h4{position:absolute;top:44px;font-family:'Roboto Condensed',sans-serif;font-weight:400;font-size:18px;color:var(--white)}
.quick-links{position:absolute;left:81px;top:83px;list-style:none;font-size:12.5px;line-height:29.5px}
.newsletter-text{position:absolute;left:254px;top:80px;width:230px;font-size:12px;line-height:23px}
.email-field{position:absolute;left:254px;top:139px;width:233px;height:33px;background:#555b67;color:var(--white);font-size:12px;line-height:33px;padding-left:14px}
.subscribe{position:absolute;left:254px;top:182px;width:116px;height:32px;background:var(--blue);color:var(--white);font-family:'Roboto Condensed',sans-serif;font-size:16px;line-height:32px;text-align:center}
.contact-details{position:absolute;left:572px;top:80px;font-size:12.5px;line-height:23px}
.footer .social{position:absolute;left:574px;top:193px;display:flex;gap:7px}
.footer .social i{width:19px;height:19px}
.map{position:absolute;left:825px;top:49px;width:294px;height:159px;background:linear-gradient(135deg,#e8e4d6,#d6e0c6 45%,#c9dbe6 70%,#e6e1d3)}
.map-link{position:absolute;left:825px;top:215px;font-size:12px;color:var(--footer-text);text-decoration:underline}
.copyright{position:absolute;left:0;top:2471px;width:1200px;height:54px;background:var(--footer-deep);color:#ddd;font-size:13.5px;line-height:54px;text-align:center}
.copyright strong{color:var(--white)}
</style>
</head>
<body>
<div class="wrap">

  <div class="topbar">
    <div class="contact">
      <span><svg width="11" height="15" viewBox="0 0 11 15"><path d="M5.5 0C2.5 0 0 2.4 0 5.4 0 9.4 5.5 15 5.5 15S11 9.4 11 5.4C11 2.4 8.5 0 5.5 0zm0 7.5a2 2 0 110-4 2 2 0 010 4z" fill="#0ea5d6"/></svg>14b 2275 Harlow Rd, Upper Fernbrook</span>
      <span><svg width="14" height="10" viewBox="0 0 14 10"><rect width="14" height="10" fill="#0ea5d6"/><path d="M0 0l7 6 7-6" stroke="#333" fill="none"/></svg>info@zem.com.au</span>
    </div>
    <div class="social"><i></i><i></i><i></i><i></i></div>
    <div class="call-now">Call Now! + 1300 482 615</div>
  </div>

  <header class="header">
    <div class="brand"><span class="mark"></span><span class="name">ZEM Technologies</span></div>
    <nav class="nav">
      <a style="left:583px">Home</a>
      <span class="sep" style="left:668px"></span>
      <a style="left:705px">About Us</a>
      <span class="sep" style="left:794px"></span>
      <a style="left:830px">Services</a>
      <span class="sep" style="left:915px"></span>
      <a style="left:951px">App's</a>
      <span class="sep" style="left:1020px"></span>
      <a style="left:1057px">Contact Us</a>
    </nav>
  </header>

  <section class="hero" role="img" aria-label="Close-up photo of a hand placing a blue jigsaw puzzle piece">
    <h1>We Literally Do Whatever It Takes<br>To Get Clients Back On Track</h1>
    <div class="dots"><i></i><i></i><i></i><i></i></div>
  </section>

  <section class="services">
    <div class="service" style="left:79px">
      <svg class="icon" width="80" height="80" viewBox="0 0 80 80" fill="#0ea5d6" stroke="#0ea5d6" stroke-width="3">
        <circle cx="40" cy="20" r="9" stroke="none"/>
        <path d="M24 48c0-10 7-16 16-16s16 6 16 16z" stroke="none"/>
        <line x1="40" y1="48" x2="40" y2="66"/><line x1="24" y1="44" x2="10" y2="56"/><line x1="56" y1="44" x2="70" y2="56"/>
        <circle cx="40" cy="69" r="5" stroke="none"/><circle cx="8" cy="58" r="5" stroke="none"/><circle cx="72" cy="58" r="5" stroke="none"/>
        <circle cx="14" cy="36" r="4" stroke="none"/><circle cx="66" cy="36" r="4" stroke="none"/>
      </svg>
      <h3>Managed IT</h3>
      <p>Clients in all industries outsource ZEM Technologies for Onsite Server Maintenance Plans and Managed IT Services.</p>
      <span class="more">+</span>
    </div>
    <div class="service" style="left:350px">
      <svg class="icon" width="80" height="80" viewBox="0 0 80 80" fill="none" stroke="#0ea5d6" stroke-width="4">
        <path d="M20 66h40a16 16 0 000-32 20 20 0 00-38-4A18 18 0 0020 66z"/>
        <rect x="42" y="26" width="22" height="18" fill="#0ea5d6" stroke="none"/>
        <path d="M46 26v-6a7 7 0 0114 0v6"/>
      </svg>
      <h3>Private Cloud</h3>
      <p>ZEM Technologies provides the design, support and maintenance for quality I.T Systems for clients to</p>
      <span class="more">+</span>
    </div>
    <div class="service" style="left:623px">
      <svg class="icon" width="80" height="80" viewBox="0 0 80 80" fill="#0ea5d6">
        <rect x="12" y="4" width="56" height="14" rx="5"/><rect x="12" y="22" width="56" height="14" rx="5"/><rect x="12" y="40" width="56" height="14" rx="5"/>
        <rect x="38" y="54" width="4" height="12"/><rect x="14" y="66" width="52" height="4"/><rect x="34" y="62" width="12" height="12"/>
        <circle cx="58" cy="11" r="2" fill="#fff"/><circle cx="58" cy="29" r="2" fill="#fff"/><circle cx="58" cy="47" r="2" fill="#fff"/>
      </svg>
      <h3>Servers</h3>
      <p>ZEM Technologies System Design solutions give clients whatever they need to pursue their business objectives.</p>
      <span class="more">+</span>
    </div>
    <div class="service" style="left:894px">
      <svg class="icon" width="80" height="80" viewBox="0 0 80 80" fill="none" stroke="#0ea5d6" stroke-width="3">
        <circle cx="40" cy="44" r="16"/><ellipse cx="40" cy="44" rx="7" ry="16"/><line x1="24" y1="44" x2="56" y2="44"/>
        <line x1="40" y1="28" x2="40" y2="14"/><line x1="26" y1="34" x2="14" y2="26"/><line x1="54" y1="34" x2="66" y2="26"/><line x1="24" y1="52" x2="10" y2="58"/><line x1="56" y1="52" x2="70" y2="58"/>
        <g fill="#0ea5d6" stroke="none"><rect x="34" y="4" width="12" height="10"/><rect x="4" y="20" width="12" height="10"/><rect x="64" y="20" width="12" height="10"/><rect x="2" y="54" width="12" height="10"/><rect x="66" y="54" width="12" height="10"/></g>
      </svg>
      <h3>Internet Solutions</h3>
      <p>ZEM Technologies is a Telvanta, Opzira and Quellnet partner. We have access to a different Tier of support so can get things</p>
      <span class="more">+</span>
    </div>
  </section>

  <section class="about">
    <h2 class="section-title"><em>About</em> ZEM Technologies</h2>
    <span class="rule"></span>
    <div class="copy">
      <p>What would it take for your information systems to actually improve the performance of your organisation?</p>
      <p>Through ZEM Technologies, companies outsource all the expertise they need to secure their systems and optimise the output of their people and IT resources – without the expense of maintaining large internal IT departments.</p>
    </div>
    <div class="btn">READ MORE</div>
    <div class="frame"></div>
    <div class="photo" role="img" aria-label="Photo of a smiling business team in suits standing in an office"></div>
  </section>

  <section class="testimonials" role="img" aria-label="Dimmed photo of a person working on a laptop in a dark office">
    <h2 class="section-title"><em>Client</em> Testimonials</h2>
    <span class="rule"></span>
    <div class="quote" style="left:81px"><svg width="42" height="26" viewBox="0 0 42 26" fill="#0ea5d6"><path d="M0 26V12L8 0h6L9 12h7v14zM22 26V12L30 0h6l-5 12h7v14z"/></svg><p>Lorem ipsum dolor sit amet, consectetuer adipiscing elit, sed diam noeenummy nibh euismod tincidunt ut laoreet doloeere magna aliquam erat volutpat. Ut wisi enieem ad minim veniam, quis nostrud exerci tation.</p></div>
    <div class="quote" style="left:434px"><svg width="42" height="26" viewBox="0 0 42 26" fill="#0ea5d6"><path d="M0 26V12L8 0h6L9 12h7v14zM22 26V12L30 0h6l-5 12h7v14z"/></svg><p>Lorem ipsum dolor sit amet, consectetuer adipiscing elit, sed diam noeenummy nibh euismod tincidunt ut laoreet doloeere magna aliquam erat volutpat. Ut wisi enieem ad minim veniam, quis nostrud exerci tation.</p></div>
    <div class="quote" style="left:786px"><svg width="42" height="26" viewBox="0 0 42 26" fill="#0ea5d6"><path d="M0 26V12L8 0h6L9 12h7v14zM22 26V12L30 0h6l-5 12h7v14z"/></svg><p>Lorem ipsum dolor sit amet, consectetuer adipiscing elit, sed diam noeenummy nibh euismod tincidunt ut laoreet doloeere magna aliquam erat volutpat. Ut wisi enieem ad minim veniam, quis nostrud exerci tation.</p></div>
    <div class="author" style="left:113px"><span class="avatar" role="img" aria-label="Client portrait"></span><div><strong>Lorem ipsum</strong><span>Lorem ipsum dolor sit</span></div></div>
    <div class="author" style="left:464px"><span class="avatar" role="img" aria-label="Client portrait"></span><div><strong>Lorem ipsum</strong><span>Lorem ipsum dolor sit</span></div></div>
    <div class="author" style="left:817px"><span class="avatar" role="img" aria-label="Client portrait"></span><div><strong>Lorem ipsum</strong><span>Lorem ipsum dolor sit</span></div></div>
    <div class="dots"><i></i><i></i><i></i></div>
  </section>

  <section class="partners">
    <h2 class="section-title"><em>Our</em> Partners</h2>
    <span class="rule"></span>
    <div class="partner" style="left:81px"><i></i></div>
    <div class="partner" style="left:259px"><i></i></div>
    <div class="partner" style="left:437px"><i></i></div>
    <div class="partner" style="left:615px"><i></i></div>
    <div class="partner" style="left:793px"><i></i></div>
    <div class="partner" style="left:971px"><i></i></div>
  </section>

  <footer class="footer">
    <h4 style="left:79px">Quick Links</h4>
    <ul class="quick-links"><li>- Home</li><li>- About Us</li><li>- Services</li><li>- App's</li><li>- Contact Us</li></ul>
    <h4 style="left:254px">Join Our Newsletter</h4>
    <p class="newsletter-text">Subscribe to our Newsletter to get the latest scoop right to your inbox</p>
    <div class="email-field">Enter Your Email</div>
    <div class="subscribe">SUBMIT</div>
    <h4 style="left:572px">Contact Details</h4>
    <p class="contact-details">1234 Street Name, City Name,<br>United States<br>123- 456- 7890<br>info@zem.com.au</p>
    <div class="social"><i></i><i></i><i></i><i></i></div>
    <div class="map" role="img" aria-label="Street map showing the office location"></div>
    <a class="map-link">View Location Map</a>
  </footer>

  <div class="copyright">Copyright © 2017 <strong>ZEM Technologies</strong> | All Rights Reserved.</div>
</div>
</body>
</html>
```